Australian Software Consultancy needs new Business Card Design

Design Business Card based on existing design artefacts (attached). We are open to all designs. As its a 2 sided design and we thought it might be quite striking to have one side with a black background and te other side with a white background.

Target Market(s)

Financial Services mainly.

Industry/Entity Type

Business

Contact Information for Business Card

Name :
Position :
Email :

Requirements
Must have
• Funky design using our existing assets

```html
<!DOCTYPE html>
<html lang="en">
<head>
<meta charset="utf-8">
<title>Clearview Labs – Business Card</title>
<link rel="stylesheet" href="https://fonts.googleapis.com/css2?family=Open+Sans:wght@400;600;700&display=swap">
<style>
  :root {
    --backdrop: #e7e4e0;
    --card-white: #ffffff;
    --card-black: #000000;
    --brand-red: #e3222b;
    --ink: #1c1c1c;
    --ink-soft: #4a4a4a;
    --rule: #bdbdbd;
    --on-dark: #ffffff;
  }
  * { box-sizing: border-box; margin: 0; padding: 0; }
  html, body {
    width: 1200px; height: 987px; overflow: hidden;
    background: var(--backdrop);
    font-family: "Open Sans", Arial, sans-serif;
  }
  .stage { position: relative; width: 1200px; height: 987px; }
  .card {
    position: absolute; width: 615px; height: 351px; overflow: hidden;
    box-shadow: 0 3px 10px rgba(0,0,0,.25);
  }
  .card--front { left: 293px; top: 130px; background: var(--card-white); }
  .card--back  { left: 292px; top: 506px; background: var(--card-black); }

  .brand {
    position: absolute; display: flex; align-items: center; gap: 12px;
  }
  .brand__mark { width: 18px; height: 18px; background: var(--brand-red); flex: none; }
  .brand__name { font-weight: 700; letter-spacing: .5px; white-space: nowrap; line-height: 1; }
  .card--front .brand { right: 43px; top: 118px; }
  .card--front .brand__name { font-size: 27px; color: var(--ink); }

  .person { position: absolute; left: 36px; top: 170px; }
  .person__name { color: var(--brand-red); font-size: 20px; font-weight: 600; line-height: 1.2; }
  .person__role { color: var(--ink); font-size: 15px; line-height: 1.4; margin-top: 2px; }
  .front__rule {
    position: absolute; left: 36px; right: 43px; top: 224px;
    border-top: 1px solid var(--rule);
  }
  .contacts { position: absolute; left: 38px; top: 235px; list-style: none; }
  .contacts li {
    display: flex; align-items: center; height: 23.5px;
    font-size: 14.5px; color: var(--ink-soft);
  }
  .contacts svg { width: 15px; height: 15px; margin-right: 8px; fill: var(--brand-red); flex: none; }
  .address {
    position: absolute; right: 43px; top: 262px; text-align: right;
    font-size: 14.5px; line-height: 23px; color: var(--ink-soft); font-style: normal;
  }
  .address__web { color: var(--brand-red); letter-spacing: 2px; }

  .card--back .brand { left: 0; right: 0; top: 196px; justify-content: center; gap: 14px; }
  .card--back .brand__mark { width: 24px; height: 24px; }
  .card--back .brand__name { font-size: 36px; color: var(--on-dark); }
  .back__web {
    position: absolute; left: 0; right: 0; top: 296px; text-align: center;
    color: var(--on-dark); font-size: 15px; letter-spacing: 3.5px;
  }
</style>
</head>
<body>
<main class="stage">
  <section class="card card--front" aria-label="Business card front">
    <div class="brand">
      <div class="brand__mark"></div>
      <div class="brand__name">CLEARVIEW LABS</div>
    </div>
    <div class="person">
      <h1 class="person__name">DANIEL HART</h1>
      <p class="person__role">CEO/FOUNDER</p>
    </div>
    <div class="front__rule"></div>
    <ul class="contacts">
      <li><svg viewBox="0 0 16 16"><path d="M3.5 1l3 3-1.6 2a9 9 0 0 0 5.1 5.1l2-1.6 3 3-2 2.5C7.5 15 1 8.5 1 3z"/></svg>612 555 0148</li>
      <li><svg viewBox="0 0 16 16"><path d="M4 0h8a1 1 0 0 1 1 1v14a1 1 0 0 1-1 1H4a1 1 0 0 1-1-1V1a1 1 0 0 1 1-1zm1 2v10h6V2zm3 11a1 1 0 1 0 0 2 1 1 0 0 0 0-2z"/></svg>614 555 0192</li>
      <li><svg viewBox="0 0 16 16"><path d="M4 1h8v4H4zM1 6h14v7h-3v2H4v-2H1zm4 5v3h6v-3z"/></svg>612 555 0177</li>
      <li><svg viewBox="0 0 16 16"><path d="M1 3h14v1.2L8 9 1 4.2zm0 2.6l7 4.8 7-4.8V13H1z"/></svg>hello@clearviewlabs.com</li>
    </ul>
    <address class="address">
      214 Harbour Street<br>
      Brisbane, Queensland 4000<br>
      <span class="address__web">www.clearviewlabs.com</span>
    </address>
  </section>

  <section class="card card--back" aria-label="Business card back">
    <div class="brand">
      <div class="brand__mark"></div>
      <div class="brand__name">CLEARVIEW LABS</div>
    </div>
    <p class="back__web">www.clearviewlabs.com</p>
  </section>
</main>
</body>
</html>
```